Brindle Huddle Post Card for Personal Promotion

This is a new application soon to be released on the market in the US.

A web site is underdevelopment but the current link is:
http://www.brindlehuddle-example.com/index_BACKUP.html

This application is intended to help a project manager or administrator schedule, deliver and communication activities for a group meeting. The application is organized around the following areas:

Scheduled Meetings
Meetings Underway
Completed Meetings
Canceled Meetings

Scheduling Phase
* Multiple facilitator-defined roles to organize meeting activities and communication
* Meeting Objective
* Pre-Meeting Instructions
* Pre-Meeting Attachments including the agenda in PDF format
* Multiple Administrators (requires BrindleHuddle license for each administrator)
* Conference/Teleconference Contact Information
* System generated comments for speakers outlining date, time and location
* Agenda Management with Breakout Session Support
* Sends email meeting invites with calendar invite, agenda and attachments

Meeting Underway Phase
* Displays current time, remaining meeting time and remaining session time to help keep meetings on schedule
* Attendance Tracking to mark when a participant arrives
* Activity Log provides quick access to meeting activities
* Up to date meeting minutes created on demand
* Session specific attachments
* Documentation of meeting action items, decisions, notes, potential risks and known issues

Completed Phase
* Role specific post meeting communications
* Optional inclusion of original agenda in PDF format
* Optional inclusion of all attachments including session attachments (up to 20 per meeting)
* Optional inclusion of user specific action items
* Follow up reminders (user defined days before due date) for participants that have action items

Canceled
* Send customized message to participants

Target Market(s)

Business people who schedule and lead meetings.

Font styles to use
Serif

Colors
faa54b
33b8a4

Requirements
Must have
• call to action: go to web site (www.brindlehuddle-example.com)
• Include color scheme from logo

```html
<!DOCTYPE html>
<html lang="en">
<head>
<meta charset="utf-8">
<title>Brindle Huddle Postcard</title>
<link href="https://fonts.googleapis.com/css2?family=Open+Sans:wght@400;600;700&display=swap" rel="stylesheet">
<style>
  :root {
    --navy: #0d1b2e;
    --navy-mid: #16304a;
    --orange: #f07a55;
    --orange-light: #faa54b;
    --teal: #33b8a4;
    --teal-light: #9ff3ef;
    --teal-dark: #4aa5a3;
    --ink: #10233a;
    --paper: #ffffff;
    --backdrop: #e9e4dc;
    --rule: #6b6b6b;
  }
  * { margin: 0; padding: 0; box-sizing: border-box; }
  html, body { width: 850px; height: 1200px; overflow: hidden; }
  body {
    background: var(--backdrop);
    font-family: "Open Sans", Arial, sans-serif;
    position: relative;
  }
  .card {
    position: absolute;
    left: 106px;
    width: 638px;
    height: 490px;
    overflow: hidden;
    box-shadow: 0 6px 14px rgba(0,0,0,.35);
  }
  .card--front { top: 88px; background: linear-gradient(135deg, var(--navy-mid), var(--navy) 60%); }
  .card--back { top: 623px; background: var(--paper); }
  .card svg.shapes { position: absolute; inset: 0; }
  .brand-name {
    position: absolute;
    font-weight: 400;
    color: var(--orange);
    white-space: nowrap;
    display: flex;
    align-items: center;
    gap: 8px;
  }
  .brand-name .dot {
    width: 12px; height: 12px; border-radius: 50%;
    background: var(--orange);
  }
  .card--back .brand-name .dot { width: 8px; height: 8px; }
  .card--front .brand-name { left: 17px; top: 42px; font-size: 30px; letter-spacing: .5px; }
  .card--back .brand-name { left: 344px; top: 38px; font-size: 19px; }
  .tagline { position: absolute; left: 17px; top: 115px; color: #fff; white-space: nowrap; }
  .tagline__kicker { color: var(--orange); font-size: 17px; letter-spacing: .3px; }
  .tagline__title { font-weight: 700; font-size: 20px; letter-spacing: .4px; margin-top: 2px; }
  .tagline__sub { font-weight: 700; font-size: 10.5px; margin-top: 4px; }
  .phases { position: absolute; left: 17px; top: 209px; list-style: none; }
  .phases li {
    display: flex; align-items: center; gap: 13px;
    height: 40px; color: #fff; font-size: 16px; white-space: nowrap;
  }
  .phases svg { width: 32px; height: 32px; }
  .contact-band {
    position: absolute; left: 0; top: 392px; width: 100%; height: 98px;
    background: linear-gradient(90deg, var(--teal-dark), var(--teal-light) 55%, var(--teal) 100%);
  }
  .address {
    position: absolute; left: 15px; top: 408px;
    display: flex; gap: 10px; color: var(--ink);
    font-weight: 700; font-size: 15px; line-height: 22px; white-space: nowrap;
  }
  .address svg { width: 18px; height: 22px; }
  .divider { position: absolute; left: 246px; top: 404px; width: 1px; height: 76px; background: var(--ink); opacity: .6; }
  .call { position: absolute; left: 256px; top: 412px; color: var(--ink); font-weight: 700; text-align: right; width: 168px; white-space: nowrap; }
  .call__label { font-size: 22px; line-height: 28px; }
  .call__number { font-size: 24px; line-height: 30px; }
  .pill {
    position: absolute; left: 0;
    background: linear-gradient(90deg, var(--teal), var(--teal-light));
    border-radius: 0 16px 16px 0;
    color: var(--ink); font-weight: 700; font-size: 16px;
    height: 31px; line-height: 31px; padding-left: 17px;
    white-space: nowrap; overflow: hidden;
  }
  .pill--cost { top: 30px; width: 162px; }
  .pill--included { top: 143px; width: 195px; }
  .pill--url {
    left: 17px; top: 376px; width: 259px; border-radius: 16px; padding-left: 0;
    text-align: center; font-size: 14px; letter-spacing: -.1px;
  }
  .copy { position: absolute; left: 17px; color: #fff; font-size: 14px; line-height: 20px; white-space: nowrap; }
  .copy--cost { top: 73px; }
  .copy--included { top: 185px; }
  .stamp-box { position: absolute; left: 531px; top: 23px; width: 86px; height: 86px; border: 1.5px solid #222; }
  .address-line { position: absolute; left: 394px; width: 222px; height: 1px; background: var(--rule); }
  .address-line--1 { top: 270px; }
  .address-line--2 { top: 309px; }
  .address-line--3 { top: 348px; }
</style>
</head>
<body>

<section class="card card--front">
  <svg class="shapes" viewBox="0 0 638 490" aria-hidden="true">
    <defs>
      <linearGradient id="photoTone" x1="0" y1="0" x2="1" y2="1">
        <stop offset="0" stop-color="#c9cdd2"/>
        <stop offset=".5" stop-color="#e6e8ea"/>
        <stop offset="1" stop-color="#9aa0a6"/>
      </linearGradient>
    </defs>
  </svg>

  <div class="contact-band"></div>

  <svg class="shapes" viewBox="0 0 638 490">
    <path role="img" aria-label="Photo of a tablet showing a planner calendar with people meeting in the background"
          d="M640 -2 C300 20 130 330 640 492 Z" fill="url(#photoTone)"/>
    <path d="M640 -2 C300 20 130 330 640 492" fill="none" stroke="#0b1626" stroke-width="22" transform="translate(-14 0)"/>
    <path d="M640 -2 C300 20 130 330 640 492" fill="none" stroke="var(--teal)" stroke-width="6" transform="translate(-10 0)"/>
    <path d="M640 -2 C300 20 130 330 640 492" fill="none" stroke="var(--orange)" stroke-width="14"/>
  </svg>

  <div class="brand-name"><span>Brindle Huddle</span><span class="dot"></span></div>

  <div class="tagline">
    <div class="tagline__kicker">MEETING MANAGEMENT</div>
    <div class="tagline__title">A PRODUCTIVITY TOOL FOR</div>
    <div class="tagline__sub">PROJECT MANAGERS AND MEETING FACILITATORS</div>
  </div>

  <ul class="phases">
    <li><svg viewBox="0 0 32 32" aria-hidden="true"><polygon points="16,1 29,8.5 29,23.5 16,31 3,23.5 3,8.5" fill="var(--orange)" stroke="#fff" stroke-width="1.5"/><rect x="10" y="10" width="12" height="12" fill="none" stroke="#fff" stroke-width="1.5"/><line x1="10" y1="14" x2="22" y2="14" stroke="#fff" stroke-width="1.5"/></svg>Scheduled Meetings</li>
    <li><svg viewBox="0 0 32 32" aria-hidden="true"><polygon points="16,1 29,8.5 29,23.5 16,31 3,23.5 3,8.5" fill="var(--orange)" stroke="#fff" stroke-width="1.5"/><circle cx="12" cy="13" r="2.5" fill="#fff"/><circle cx="20" cy="13" r="2.5" fill="#fff"/><rect x="9" y="17" width="14" height="5" rx="2" fill="#fff"/></svg>Meetings Underway</li>
    <li><svg viewBox="0 0 32 32" aria-hidden="true"><polygon points="16,1 29,8.5 29,23.5 16,31 3,23.5 3,8.5" fill="var(--orange)" stroke="#fff" stroke-width="1.5"/><rect x="10" y="9" width="11" height="14" fill="none" stroke="#fff" stroke-width="1.5"/><polyline points="13,17 16,20 22,13" fill="none" stroke="#fff" stroke-width="1.8"/></svg>Completed Meetings</li>
    <li><svg viewBox="0 0 32 32" aria-hidden="true"><polygon points="16,1 29,8.5 29,23.5 16,31 3,23.5 3,8.5" fill="var(--orange)" stroke="#fff" stroke-width="1.5"/><rect x="10" y="10" width="12" height="12" fill="none" stroke="#fff" stroke-width="1.5"/><line x1="10" y1="14" x2="22" y2="14" stroke="#fff" stroke-width="1.5"/><line x1="13" y1="17" x2="19" y2="17" stroke="#fff" stroke-width="1.2"/></svg>Canceled Meetings</li>
  </ul>

  <div class="address">
    <svg viewBox="0 0 18 22" aria-hidden="true"><path d="M9 1a7 7 0 0 0-7 7c0 5 7 13 7 13s7-8 7-13a7 7 0 0 0-7-7z" fill="none" stroke="var(--ink)" stroke-width="2"/><circle cx="9" cy="8" r="2.5" fill="var(--ink)"/></svg>
    <div>Harrowgate Systems, Inc.<br>PO Box 4182<br>Millbrook, Virginia 24099</div>
  </div>
  <div class="divider"></div>
  <div class="call">
    <div class="call__label">Call US:</div>
    <div class="call__number">555-014-2273</div>
  </div>
</section>

<section class="card card--back">
  <svg class="shapes" viewBox="0 0 638 490">
    <defs>
      <linearGradient id="panelTone" x1="0" y1="0" x2="1" y2="1">
        <stop offset="0" stop-color="var(--navy-mid)"/>
        <stop offset="1" stop-color="var(--navy)"/>
      </linearGradient>
    </defs>
    <path d="M0 0 H224 C330 90 380 260 294 408 H0 Z" fill="url(#panelTone)"/>
    <path d="M224 0 C330 90 380 260 294 408" fill="none" stroke="var(--teal)" stroke-width="4" transform="translate(6 0)"/>
    <path d="M222 -2 H250 C350 90 372 270 294 408 C352 260 320 90 222 -2 Z" fill="var(--orange)"/>
  </svg>

  <div class="pill pill--cost">WHAT IS COST</div>
  <p class="copy copy--cost">The current introductory price is<br>reduced from $179 to $150 until<br>January 1st, 2018.</p>

  <div class="pill pill--included">WHAT IS INCLUDED</div>
  <p class="copy copy--included">Unlimited meetings during the<br>subscription period. Total number of<br>participants per meeting is currently<br>one-hundred (100). Up to 20 email<br>attachments are possible for meeting<br>invites and minutes--not including the<br>agenda or meeting minutes. Contact<br>us if you need more than 100 people<br>or additional attachments to emails.</p>

  <div class="pill pill--url">www.brindlehuddle-example.com</div>

  <div class="brand-name"><span>Brindle Huddle</span><span class="dot"></span></div>
  <div class="stamp-box"></div>
  <div class="address-line address-line--1"></div>
  <div class="address-line address-line--2"></div>
  <div class="address-line address-line--3"></div>
</section>

</body>
</html>
```